Tarvek Mailbox Services, full-service collaboration with postal service - installation of units

1. CBU - Cluster Box Unit - These are Mailbox units that you would see at residential neighborhoods, and Apartments -
2. Logo Needed
3. Maybe have CBU as a division of DWHS (Tarvek Mailbox Services)
4. Card to be primary Tarvek Mailbox Services

This is a letter of introduction that I am developing:

I am writing to introduce Tarvek Mailbox Services, a company dedicated to delivering exceptional service and quality in the installation and maintenance of commercial mailboxes, specifically Cluster Box Units (CBUs). Our commitment to excellence and customer satisfaction has established us as a trusted partner for developers and postal services alike.
At Tarvek Mailbox Services, we take pride in our comprehensive approach, ensuring that every step of the mailbox installation process is handled with precision and care. Our services include:
• Supplying high-quality CBUs tailored to meet the specific needs of your development.
• Providing a CBU plat layout upon approval of the address plat, ensuring seamless integration into your development plans.
• Collaborating with developers and postmasters to determine the optimal CBU locations for efficient mail delivery.
• Qualifying the labeling of CBU units, offering both sticker and etching options to suit your preferences.
• Pouring durable concrete foundations as required for the secure installation of the CBU units.
• Handling the installation process with expertise and attention to detail.
• Labeling the units and supplying keys for each mailbox, ensuring a smooth transition for residents and businesses.
Our team is dedicated to working closely with you to ensure that all requirements are met and that the installation process is completed efficiently and to the highest standards.
We look forward to the opportunity to collaborate with you and contribute to the success of your project. Please do not hesitate to contact us for any additional information or to discuss your specific requirements.
Sincerely,
Dorian Whitcombe
Tarvek Mailbox Services

Target Market(s)

Developers, Builders, Apartment's, HOA

Industry/Entity Type

Construction

Contact Information for Business Card

Name: Dorian Whitcombe, Cell:555-017-6481, Email: dori@dwhomeworks.example

Font styles to use
Serif

Requirements
Must have
• Fresh Looking
Nice to have
• Maybe a CBU Box if it looks clean
Should not have
• Not Industrial or Old traditional card

```html
<!DOCTYPE html>
<html lang="en">
<head>
<meta charset="utf-8">
<title>Tarvek Mailbox Services – Business Card</title>
<link rel="stylesheet" href="https://fonts.googleapis.com/css2?family=Playfair+Display:wght@600;700&family=Roboto:wght@400&display=swap">
<style>
  :root {
    --backdrop: #e3e3e3;
    --card-white: #ffffff;
    --brand-maroon: #740d2d;
    --text-grey: #555555;
    --rule-dark: #333333;
  }
  * { margin: 0; padding: 0; box-sizing: border-box; }
  html, body {
    width: 1188px; height: 1200px; overflow: hidden;
    background: var(--backdrop);
  }
  .canvas { position: relative; width: 1188px; height: 1200px; }
  .card {
    position: absolute; left: 245px; width: 696px; height: 386px;
  }
  .card--front { top: 159px; background: var(--card-white); }
  .card--back { top: 627px; background: var(--brand-maroon); }

  /* Front brand lockup */
  .brand-lockup {
    position: absolute; left: 64px; top: 51px;
    display: flex; align-items: center; gap: 14px;
  }
  .brand-mark { width: 86px; height: 86px; background: var(--brand-maroon); flex: none; }
  .brand-text { display: flex; flex-direction: column; align-items: stretch; }
  .brand-name {
    font-family: "Playfair Display", serif; font-weight: 700;
    font-size: 40px; line-height: 1; letter-spacing: 2px;
    color: var(--brand-maroon); text-transform: uppercase; text-align: center;
  }
  .brand-tagline {
    display: flex; align-items: center; gap: 8px; margin-top: 6px;
    font-family: "Playfair Display", serif; font-weight: 600;
    font-size: 15px; letter-spacing: 1px; text-transform: uppercase;
    color: var(--rule-dark); white-space: nowrap;
  }
  .brand-tagline::before, .brand-tagline::after {
    content: ""; flex: 1; min-width: 40px; height: 2px; background: var(--rule-dark);
  }

  .cabinet-art {
    position: absolute; left: 483px; top: 141px; width: 180px; height: 210px;
    background: linear-gradient(180deg, #f7f7f7, #f1f1f1);
  }

  /* Card holder */
  .holder { position: absolute; left: 179px; top: 193px; }
  .holder-name {
    font-family: "Playfair Display", serif; font-weight: 700;
    font-size: 25px; color: var(--brand-maroon); line-height: 1.05;
    text-transform: uppercase; letter-spacing: 0.5px;
  }
  .holder-title {
    font-family: "Roboto", sans-serif; font-size: 18px;
    color: var(--text-grey); line-height: 1.2;
  }
  .contact-list { list-style: none; margin-top: 20px; }
  .contact-item {
    display: flex; align-items: center; gap: 10px; height: 23px;
    font-family: "Roboto", sans-serif; font-size: 18px; color: var(--text-grey);
  }
  .contact-icon { width: 19px; height: 19px; flex: none; fill: var(--brand-maroon); }

  /* Back */
  .back-lockup {
    position: absolute; left: 0; right: 0; top: 92px;
    display: flex; flex-direction: column; align-items: center;
  }
  .back-lockup .brand-mark { width: 120px; height: 120px; background: var(--card-white); }
  .back-lockup .brand-text { margin-top: 20px; width: 376px; }
  .back-lockup .brand-name { color: var(--card-white); font-size: 44px; }
  .back-lockup .brand-tagline { color: var(--card-white); font-size: 17px; margin-top: 8px; }
  .back-lockup .brand-tagline::before,
  .back-lockup .brand-tagline::after { background: var(--card-white); }
</style>
</head>
<body>
<div class="canvas">
  <section class="card card--front">
    <div class="brand-lockup">
      <div class="brand-mark"></div>
      <div class="brand-text">
        <p class="brand-name">Tarvek</p>
        <p class="brand-tagline">Mailbox Services</p>
      </div>
    </div>

    <div class="cabinet-art" role="img" aria-label="Faint line illustration of a cluster mailbox unit on a pedestal"></div>

    <div class="holder">
      <p class="holder-name">Dorian Whitcombe</p>
      <p class="holder-title">Managing Director</p>
      <ul class="contact-list">
        <li class="contact-item">
          <svg class="contact-icon" viewBox="0 0 20 20" aria-hidden="true"><path d="M1 7c0-3 4-5 9-5s9 2 9 5v1h-5V6H6v2H1z"/><path d="M4 10l2-3h8l2 3v8H4z"/><circle cx="10" cy="13" r="2.5" fill="#fff"/></svg>
          <span>555-017-6481</span>
        </li>
        <li class="contact-item">
          <svg class="contact-icon" viewBox="0 0 20 20" aria-hidden="true"><path d="M1 4h18v2l-9 5-9-5z"/><path d="M1 8l9 5 9-5v8H1z"/></svg>
          <span>dori@dwhomeworks.example</span>
        </li>
        <li class="contact-item">
          <svg class="contact-icon" viewBox="0 0 20 20" aria-hidden="true"><circle cx="10" cy="10" r="9"/><path d="M5 5c2 0 3 1 3 3s-2 2-2 4 1 3 0 4c-2-1-3-3-3-6 0-2 1-4 2-5zM12 3c2 1 1 3 3 3 1 0 2 2 1 4-1 1-2 0-3 2s0 3-1 4c-1-2-2-3-1-5s-1-3 0-5c0-1 1-2 1-3z" fill="#fff"/></svg>
          <span>www.dwhomeworks.example</span>
        </li>
      </ul>
    </div>
  </section>

  <section class="card card--back">
    <div class="back-lockup">
      <div class="brand-mark"></div>
      <div class="brand-text">
        <p class="brand-name">Tarvek</p>
        <p class="brand-tagline">Mailbox Services</p>
      </div>
    </div>
  </section>
</div>
</body>
</html>
```